依頼詳細
会社のカラーは
http://kinotesu-sample.com/

サイズは、名刺サイズでお願いします。
記載項目
●賞状のタイトル

こもれび月間AWARD
「成長」部門
「おもいやり」部門
「プロフェッショナル」部門
「最多投票」部門
※それぞれ

●受賞者の名前 フルネーム
●対象月:2016年4月

●文章:
あなたは、こもれびAWARD「●●部門」において、
もっとも多くの成果をあげ、当社の成長と発展に多大なる貢献をされました。
よってここにその功績を高く賞賛し表彰いたします。

株式会社こもれび
委員長 ●●●●
希望イメージ
シンプル 複雑
単色 カラフル
暗い 明るい
日常 高級
遊び心 厳粛
未来的 伝統的
女性的 男性的
希望する色
青系、水色系
納品ファイル
• 高解像度JPG (.jpg)
• イラストレーター形式 (.ai)
■ 選んだ理由

シンプルでうちの雰囲気に合ってるきがしました。
もらって集めてもうれしいカードになるかなと思いました。

■ 提案者全員のお礼・コメント

短い期間でしたが、たくさん応募いただきましてありがとうございます。

```html
<!DOCTYPE html>
<html lang="ja">
<head>
<meta charset="utf-8">
<title>こもれび月間AWARD カード</title>
<link rel="stylesheet" href="https://fonts.googleapis.com/css2?family=Noto+Sans+JP:wght@400;700;900&family=Noto+Serif+JP:wght@700;900&display=swap">
<style>
  :root {
    --page: #ffffff;
    --card-bg: #ffffff;
    --card-edge: #d9d9d9;
    --brand: #2a9fd0;
    --badge: #1f8fd6;
    --ink: #222222;
    --band: #4a4a4a;
    --band-dark: #2e2e2e;
    --wreath: #f1ece0;
    --growth: #159a8c;
    --growth-dark: #0d6e64;
    --care: #d44b6b;
    --care-dark: #9c2f48;
    --pro: #1c5aa8;
    --pro-dark: #123d74;
    --votes: #f0a71c;
    --votes-dark: #b87b0c;
  }
  html, body {
    margin: 0;
    padding: 0;
    width: 1200px;
    height: 3076px;
    overflow: hidden;
    background: var(--page);
  }
  .sheet {
    position: relative;
    width: 1200px;
    height: 3076px;
  }
  .award-card {
    position: absolute;
    left: 20px;
    width: 1160px;
    height: 700px;
    background: var(--card-bg);
    box-shadow: 0 0 0 2px var(--card-edge);
    overflow: hidden;
    font-family: "Noto Sans JP", sans-serif;
    color: var(--ink);
  }
  .award-card--growth { top: 24px; --accent: var(--growth); --accent-dark: var(--growth-dark); }
  .award-card--care { top: 800px; --accent: var(--care); --accent-dark: var(--care-dark); }
  .award-card--pro { top: 1576px; --accent: var(--pro); --accent-dark: var(--pro-dark); }
  .award-card--votes { top: 2352px; --accent: var(--votes); --accent-dark: var(--votes-dark); }

  .wreath {
    position: absolute;
    left: 230px;
    top: 230px;
    width: 700px;
    height: 440px;
    border-radius: 50%;
    background: radial-gradient(ellipse at center, rgba(241,236,224,0) 45%, var(--wreath) 62%, rgba(241,236,224,0) 75%);
  }
  .ribbon {
    position: absolute;
    left: 0;
    top: 0;
  }
  .ribbon .band { fill: var(--band); }
  .ribbon .band-shade { fill: var(--band-dark); }
  .ribbon .banner { fill: var(--accent); }
  .ribbon .banner-fold { fill: var(--accent-dark); }

  .brand-name {
    position: absolute;
    left: 60px;
    top: 28px;
    font-size: 64px;
    font-weight: 900;
    color: var(--brand);
    letter-spacing: 2px;
    line-height: 1;
  }
  .award-label {
    position: absolute;
    left: 400px;
    top: 42px;
    font-size: 54px;
    font-weight: 700;
    line-height: 1;
    letter-spacing: 1px;
  }
  .month-badge {
    position: absolute;
    right: 40px;
    top: 24px;
    width: 176px;
    height: 176px;
    border-radius: 50%;
    background: var(--badge);
    color: #fff;
    text-align: center;
    font-family: "Noto Serif JP", serif;
    font-weight: 700;
  }
  .month-badge .month { display: block; font-size: 72px; line-height: 1; padding-top: 26px; }
  .month-badge .year { display: block; font-size: 40px; line-height: 1; margin-top: 8px; }

  .category {
    position: absolute;
    left: 200px;
    width: 760px;
    top: 118px;
    text-align: center;
    color: #fff;
    font-family: "Noto Serif JP", serif;
    font-weight: 900;
    line-height: 1;
  }
  .category .name { display: block; font-size: 108px; letter-spacing: 12px; }
  .award-card--pro .category .name { font-size: 84px; letter-spacing: 0; padding-top: 12px; padding-bottom: 12px; }
  .award-card--care .category .name { font-size: 100px; letter-spacing: 4px; padding-top: 4px; padding-bottom: 4px; }
  .category .division { display: block; font-size: 50px; letter-spacing: 28px; margin-top: 14px; padding-left: 28px; }

  .recipient {
    position: absolute;
    left: 0;
    width: 1160px;
    top: 372px;
    text-align: center;
    font-size: 72px;
    font-weight: 700;
    line-height: 1;
  }
  .recipient .honorific { font-size: 48px; margin-left: 10px; }
  .citation {
    position: absolute;
    left: 0;
    width: 1160px;
    top: 478px;
    text-align: center;
    font-size: 27px;
    line-height: 1.45;
    margin: 0;
  }
  .signature {
    position: absolute;
    left: 0;
    width: 1160px;
    top: 620px;
    text-align: center;
    font-size: 27px;
    line-height: 1;
  }
  .signature span + span { margin-left: 36px; }
</style>
</head>
<body>
<main class="sheet">

  <section class="award-card award-card--growth">
    <div class="wreath" role="img" aria-label="月桂樹のリース装飾"></div>
    <svg class="ribbon" width="1160" height="700" viewBox="0 0 1160 700" aria-hidden="true">
      <polygon class="band" points="0,200 1160,160 1160,250 0,290"/>
      <polygon class="band-shade" points="0,270 1160,230 1160,250 0,290"/>
      <polygon class="banner-fold" points="200,340 240,340 230,370"/>
      <polygon class="banner" points="240,110 960,110 920,340 200,340"/>
    </svg>
    <div class="brand-name">こもれび</div>
    <div class="award-label">月間AWARD</div>
    <div class="month-badge"><span class="month">04</span><span class="year">2016</span></div>
    <h2 class="category"><span class="name">成長</span><span class="division">部門</span></h2>
    <div class="recipient">山田　太郎<span class="honorific">様</span></div>
    <p class="citation">あなたは、こもれびAWARD「成長部門」において、<br>もっとも多くの成果をあげ、当社の成長と発展に多大なる貢献をされました。<br>よってここにその功績を高く賞賛し表彰いたします。</p>
    <div class="signature"><span>株式会社こもれび</span><span>委員長:山田　太郎</span></div>
  </section>

  <section class="award-card award-card--care">
    <div class="wreath" role="img" aria-label="月桂樹のリース装飾"></div>
    <svg class="ribbon" width="1160" height="700" viewBox="0 0 1160 700" aria-hidden="true">
      <polygon class="band" points="0,200 1160,160 1160,250 0,290"/>
      <polygon class="band-shade" points="0,270 1160,230 1160,250 0,290"/>
      <polygon class="banner-fold" points="200,340 240,340 230,370"/>
      <polygon class="banner" points="240,110 960,110 920,340 200,340"/>
    </svg>
    <div class="brand-name">こもれび</div>
    <div class="award-label">月間AWARD</div>
    <div class="month-badge"><span class="month">04</span><span class="year">2016</span></div>
    <h2 class="category"><span class="name">おもいやり</span><span class="division">部門</span></h2>
    <div class="recipient">山田　太郎<span class="honorific">様</span></div>
    <p class="citation">あなたは、こもれびAWARD「おもいやり部門」において、<br>もっとも多くの成果をあげ、当社の成長と発展に多大なる貢献をされました。<br>よってここにその功績を高く賞賛し表彰いたします。</p>
    <div class="signature"><span>株式会社こもれび</span><span>委員長:山田　太郎</span></div>
  </section>

  <section class="award-card award-card--pro">
    <div class="wreath" role="img" aria-label="月桂樹のリース装飾"></div>
    <svg class="ribbon" width="1160" height="700" viewBox="0 0 1160 700" aria-hidden="true">
      <polygon class="band" points="0,200 1160,160 1160,250 0,290"/>
      <polygon class="band-shade" points="0,270 1160,230 1160,250 0,290"/>
      <polygon class="banner-fold" points="200,340 240,340 230,370"/>
      <polygon class="banner" points="240,110 960,110 920,340 200,340"/>
    </svg>
    <div class="brand-name">こもれび</div>
    <div class="award-label">月間AWARD</div>
    <div class="month-badge"><span class="month">04</span><span class="year">2016</span></div>
    <h2 class="category"><span class="name">プロフェッショナル</span><span class="division">部門</span></h2>
    <div class="recipient">山田　太郎<span class="honorific">様</span></div>
    <p class="citation">あなたは、こもれびAWARD「プロフェッショナル部門」において、<br>もっとも多くの成果をあげ、当社の成長と発展に多大なる貢献をされました。<br>よってここにその功績を高く賞賛し表彰いたします。</p>
    <div class="signature"><span>株式会社こもれび</span><span>委員長:山田　太郎</span></div>
  </section>

  <section class="award-card award-card--votes">
    <div class="wreath" role="img" aria-label="月桂樹のリース装飾"></div>
    <svg class="ribbon" width="1160" height="700" viewBox="0 0 1160 700" aria-hidden="true">
      <polygon class="band" points="0,200 1160,160 1160,250 0,290"/>
      <polygon class="band-shade" points="0,270 1160,230 1160,250 0,290"/>
      <polygon class="banner-fold" points="200,340 240,340 230,370"/>
      <polygon class="banner" points="240,110 960,110 920,340 200,340"/>
    </svg>
    <div class="brand-name">こもれび</div>
    <div class="award-label">月間AWARD</div>
    <div class="month-badge"><span class="month">04</span><span class="year">2016</span></div>
    <h2 class="category"><span class="name">最多投票</span><span class="division">部門</span></h2>
    <div class="recipient">山田　太郎<span class="honorific">様</span></div>
    <p class="citation">あなたは、こもれびAWARD「最多投票部門」において、<br>もっとも多くの成果をあげ、当社の成長と発展に多大なる貢献をされました。<br>よってここにその功績を高く賞賛し表彰いたします。</p>
    <div class="signature"><span>株式会社こもれび</span><span>委員長:山田　太郎</span></div>
  </section>

</main>
</body>
</html>
```